Cradlekin by Marianne Business Card Design

i am starting a new business as a reborn artist (that is painting dolls to make them look like real live babies)

i eventually want to sell the dolls that i make and have classed in reborning. but at the moment i just want to get my name out there.

I do not currently have images of the dolls so cannot have an image in the design.

Non compulsory thoughts: i like the look of old wood, white and baby pink,even hot pink, and lace, denim. i had in mind something like a tiny baby in a old cradle or something, a old drawer, box, something different or unusual, it has to be a girl baby. i am also open to other thoughts on the matter. i would like plain writing not all swirly
Updates

Sorry to change but would like it to read country cradlekin by marianne.

Reason: I have not been able to find the design I am looking for

Industry/Entity Type

Painting

Contact Information for Business Card

Cradlekin by Marianne
country babies that never grow up
Reborn Artist Marianne Holt
0437 651 840
lunet.v@mailvane.net

```html
<!DOCTYPE html>
<html lang="en">
<head>
<meta charset="utf-8">
<title>Cradlekin by Marianne – Business Card</title>
<link rel="stylesheet" href="https://fonts.googleapis.com/css2?family=Federo&family=Delius&family=Josefin+Sans:wght@600&family=Parisienne&display=swap">
<style>
  :root {
    --backdrop: #ecebe8;
    --kraft: #b48d5f;
    --kraft-deep: #9c764b;
    --whitewash: #f1ede6;
    --whitewash-shade: #e2dcd1;
    --ink: #2a211c;
    --teal-text: #4a8ea4;
    --brand-text: #fbf7f0;
    --tape-teal: #67b6bd;
    --tape-mint: #a8dccb;
    --tape-sand: #e6c79b;
    --tape-stripe: #2c2c2c;
    --square: #3d6aa6;
  }
  * { box-sizing: border-box; margin: 0; padding: 0; }
  html, body {
    width: 1200px; height: 741px; overflow: hidden;
    background: var(--backdrop);
  }
  .canvas { position: relative; width: 1200px; height: 741px; }

  .card {
    position: absolute; left: 355px; top: 40px;
    width: 490px; height: 660px;
    box-shadow: 0 6px 18px rgba(0,0,0,.18);
  }
  .card__header {
    position: absolute; left: 0; top: 0; width: 490px; height: 240px;
    background: var(--kraft);
  }
  .card__brand {
    position: absolute; left: 0; right: 0; top: 70px;
    text-align: center;
    font-family: "Federo", sans-serif;
    color: var(--brand-text);
    font-size: 52px; letter-spacing: 4px; line-height: 1.1;
  }
  .card__brand-sub { display: block; font-size: 32px; letter-spacing: 1px; }

  .card__panel {
    position: absolute; left: 36px; top: 205px; width: 420px; height: 440px;
    background: linear-gradient(90deg, var(--whitewash) 0%, var(--whitewash-shade) 50%, var(--whitewash) 100%);
    border-radius: 0 0 10px 10px;
  }

  .tape { position: absolute; }
  .tape--stripe { left: 250px; top: 22px; width: 150px; height: 30px; background: var(--tape-stripe); transform: rotate(4deg); }
  .tape--mint-top { left: 385px; top: 30px; width: 100px; height: 42px; background: var(--tape-mint); transform: rotate(4deg); }
  .tape--teal { left: 20px; top: 185px; width: 300px; height: 36px; background: var(--tape-teal); transform: rotate(2deg); }
  .tape--sand { left: 345px; top: 205px; width: 120px; height: 40px; background: var(--tape-sand); transform: rotate(1deg); }

  .card__tagline {
    position: absolute; left: 36px; top: 280px; width: 420px;
    text-align: center;
    font-family: "Delius", sans-serif; color: var(--ink);
    font-size: 27px; line-height: 1.3;
  }
  .card__role {
    position: absolute; left: 36px; top: 375px; width: 420px;
    text-align: center;
    font-family: "Josefin Sans", sans-serif; font-weight: 600;
    color: var(--teal-text); font-size: 38px;
  }
  .card__name {
    position: absolute; left: 36px; top: 428px; width: 420px;
    text-align: center;
    font-family: "Parisienne", cursive; color: var(--teal-text); font-size: 36px;
  }
  .card__phone {
    position: absolute; left: 36px; top: 482px; width: 420px;
    text-align: center;
    font-family: "Josefin Sans", sans-serif; font-weight: 600;
    color: var(--teal-text); font-size: 33px; letter-spacing: 1px;
  }
  .card__email {
    position: absolute; left: 20px; top: 530px; width: 450px;
    text-align: center;
    font-family: "Josefin Sans", sans-serif; font-weight: 600;
    color: var(--teal-text); font-size: 26px;
  }
  .card__social {
    position: absolute; left: 60px; top: 580px; width: 380px;
    display: flex; align-items: center; gap: 18px;
    font-family: "Josefin Sans", sans-serif; font-weight: 600;
    color: var(--teal-text); font-size: 28px;
  }
  .card__social-square {
    width: 44px; height: 44px; background: var(--square); border-radius: 4px; flex: none;
  }
</style>
</head>
<body>
<main class="canvas">
  <section class="card" aria-label="Cradlekin by Marianne business card">
    <div class="card__header"></div>
    <div class="card__panel"></div>

    <div class="tape tape--stripe"></div>
    <div class="tape tape--mint-top"></div>
    <div class="tape tape--teal"></div>
    <div class="tape tape--sand"></div>

    <h1 class="card__brand">CRADLEKIN <span class="card__brand-sub">by Marianne</span></h1>

    <p class="card__tagline">country babies that<br>never grow up</p>
    <p class="card__role">Reborn Artist</p>
    <p class="card__name">Marianne Holt</p>
    <p class="card__phone">0437 651 840</p>
    <p class="card__email">lunet.v@mailvane.net</p>
    <p class="card__social"><span class="card__social-square"></span>cradlekin by marianne</p>
  </section>
</main>
</body>
</html>
```